Buy LumaPass landing page redesign

I would like the following page redesigned: http://luma-pass.co.uk/lpv3/jointheclub.php
The header and footer will remain the same, but I need the content to be visually appealing.
The only requirements are the 3 card options - but the design of this can of course be completely different to what is currently there.
You can also use brand logos / names from our partner list - see http://luma-pass.co.uk/index.php or http://luma-pass.co.uk/partners for brands.
Happy to answer any questions or provide more detail, but essentially looking to make this page much more attractive in order to increase conversion - i.e. get people to buy a LumaPass
Target Market(s)
High income male and female audience
Font styles to use
Other font styles liked:
- Avenir
Colors
Designer to choose colors to be used in the design.
Requirements
Must have
- The current header and footer
The 3 card options (1 month, 6 months, 12 months)
Nice to have
- logos of partner brands could be used or else the animated gif that we currently have on the page
also the card graphics (mobile and card image) could be incorporated

```html
<!DOCTYPE html>
<html lang="en">
<head>
<meta charset="utf-8">
<title>Buy Your LumaPass</title>
<link rel="stylesheet" href="https://fonts.googleapis.com/css2?family=Nunito+Sans:wght@300;400;600;700&family=PT+Sans+Narrow:wght@400;700&display=swap">
<style>
:root{
  --ink:#111;
  --black:#000;
  --grey-text:#8a8a8a;
  --teal:#1a9dbd;
  --card-bg:#e4e4e4;
  --card-edge:#c9c9c9;
  --month-1:#aef1f1;
  --month-6:#c8a8e6;
  --month-12:#f5e596;
  --btn-top:#4d5256;
  --btn-bot:#1f2326;
  --footer-text:#e8e8e8;
  --rule:#777;
}
*{box-sizing:border-box;margin:0;padding:0}
html,body{width:796px;height:1200px;overflow:hidden;background:#fff}
body{position:relative;font-family:"Nunito Sans",sans-serif;color:var(--ink)}
.abs{position:absolute}

/* header */
.top-band{left:0;top:0;width:796px;height:9px;background:var(--black)}
.account-tab{left:554px;top:0;width:213px;height:28px;background:var(--black);color:#fff;font-size:8px;font-weight:700;text-align:center;line-height:28px;letter-spacing:-.1px}
.brand{left:19px;top:20px;font-size:37px;font-weight:400;letter-spacing:1px;color:var(--ink)}
.nav{top:47px;font-size:11.5px;color:var(--grey-text);text-transform:uppercase}

/* hero */
.hero-visual{left:0;top:72px;width:796px;height:292px;background:linear-gradient(90deg,#f07aa8 0%,#f9b7c9 18%,#f4e6ef 38%,#f8f4fa 55%,#fbf7fb 80%,#efd9ee 100%)}
.hero-rule{left:327px;top:72px;width:463px;height:3px;background:var(--black)}
.hero-title{left:338px;top:85px;font-size:30px;font-weight:400}
.hero-lead{left:338px;top:128px;font-family:"PT Sans Narrow",sans-serif;font-weight:700;font-size:18px}
.hero-body{left:338px;top:148px;width:440px;font-size:11px;line-height:13.5px}
.perks-title{left:397px;top:196px;font-family:"PT Sans Narrow",sans-serif;font-weight:700;font-size:21px;color:var(--teal)}
.perks{left:398px;top:229px;list-style:none;font-size:12.5px}
.perks li{display:flex;align-items:center;height:24.3px}
.perks svg{width:16px;height:14px;margin-right:8px}
.section-rule{left:16px;width:755px;height:3px;background:var(--black)}

/* plans */
.mascot{left:27px;top:423px;width:207px;height:218px;border-radius:20px;background:linear-gradient(160deg,#7fe0f3,#3aa6d8 60%,#2a2f35)}
.plan{top:419px;width:162px;height:227px;background:linear-gradient(180deg,#f3f3f3,var(--card-bg));border:3px solid var(--card-edge);border-radius:6px}
.plan-head{position:absolute;left:9px;top:10px;width:138px;height:30px;border-radius:4px;text-align:center;line-height:30px;font-size:15px;font-weight:400}
.plan-copy{position:absolute;left:10px;top:46px;width:136px;height:92px;background:rgba(255,255,255,.35);border-radius:4px;padding:10px 8px 0 13px;font-size:9.6px;line-height:12px}
.plan-price{position:absolute;left:10px;top:143px;font-size:9.6px;line-height:12px}
.plan-price b{font-weight:700}
.plan-btn{position:absolute;left:29px;top:176px;width:102px;height:27px;border-radius:3px;background:linear-gradient(180deg,var(--btn-top),var(--btn-bot));color:#fff;font-weight:700;font-size:15px;text-align:center;line-height:27px}
.footnote{left:0;top:670px;width:796px;text-align:center;font-family:"PT Sans Narrow",sans-serif;font-size:23px;line-height:29px}
.intro{left:0;top:763px;width:740px;text-align:center;font-size:62px;font-weight:300;line-height:70px;letter-spacing:1px}

/* footer */
.footer{left:4px;top:994px;width:788px;height:206px;background:var(--black);color:var(--footer-text)}
.f{position:absolute;font-size:11px;color:var(--footer-text)}
.field{position:absolute;height:20px;background:#fff;border:1px solid #aaa;font-size:10px;color:#999;padding-left:5px;line-height:18px}
.field.code{background:#e6e6e6}
.signup-btn{position:absolute;height:18px;background:#f2f2f2;border:1px solid #999;border-radius:3px;color:#222;font-size:10.5px;text-align:center;line-height:16px}
.social{position:absolute;top:39px;width:24px;height:24px;background:#fff}
.f-rule{position:absolute;left:32px;top:84px;width:718px;height:1px;background:var(--rule)}
.links{position:absolute;top:100px;list-style:none;font-size:11px;line-height:18.8px}
.legal{position:absolute;left:372px;top:99px;width:380px;font-size:11px;line-height:19px}
</style>
</head>
<body>

<header>
  <div class="abs top-band"></div>
  <div class="abs account-tab">SIGN UP FOR DAILY EMAIL | LOGIN</div>
  <div class="abs brand">LUMAPASS</div>
  <nav>
    <span class="abs nav" style="left:325px">What is LumaPass?</span>
    <span class="abs nav" style="left:461px">Buy a LumaPass</span>
    <span class="abs nav" style="left:578px">Daily Stories ▾</span>
    <span class="abs nav" style="left:687px">A-Z of Offers</span>
  </nav>
</header>

<section class="hero">
  <div class="abs hero-visual" role="img" aria-label="Colourful fashion photograph of a model with rainbow hair holding a black membership card"></div>
  <div class="abs hero-rule"></div>
  <h1 class="abs hero-title">Buy Your LumaPass</h1>
  <p class="abs hero-lead">Buy a LumaPass and save on fashion, beauty, restaurants &amp; more</p>
  <p class="abs hero-body">at all our partner brands each time you shop online or in-store. Start saving immediately by downloading your card straight to your mobile phone.</p>
  <h2 class="abs perks-title">What you get with your LumaPass</h2>
  <ul class="abs perks">
    <li><svg viewBox="0 0 16 14"><path d="M1 8l4 4 10-11" fill="none" stroke="#000" stroke-width="3"/></svg>Save on fashion, beauty, restaurants &amp; more</li>
    <li><svg viewBox="0 0 16 14"><path d="M1 8l4 4 10-11" fill="none" stroke="#000" stroke-width="3"/></svg>Digital LumaPass on your mobile phone</li>
    <li><svg viewBox="0 0 16 14"><path d="M1 8l4 4 10-11" fill="none" stroke="#000" stroke-width="3"/></svg>Notification of all new offers from brands</li>
    <li><svg viewBox="0 0 16 14"><path d="M1 8l4 4 10-11" fill="none" stroke="#000" stroke-width="3"/></svg>Optional weekly round-up</li>
    <li><svg viewBox="0 0 16 14"><path d="M1 8l4 4 10-11" fill="none" stroke="#000" stroke-width="3"/></svg>Reduced rate on LumaPass BLACK*</li>
  </ul>
</section>
<div class="abs section-rule" style="top:368px"></div>

<section class="plans">
  <div class="abs mascot" role="img" aria-label="Cartoon superhero mascot pointing at a smartphone showing the card"></div>

  <article class="abs plan" style="left:263px">
    <div class="plan-head" style="background:var(--month-1)">1 MONTH</div>
    <p class="plan-copy">A one month LumaPass is perfect ahead of a shopping spree. Whether you're buying gifts for friends, family or yourself, LumaPass is here to help.</p>
    <p class="plan-price">Price: <b>£4.99</b><br>For 1 Month</p>
    <div class="plan-btn">BUY NOW</div>
  </article>

  <article class="abs plan" style="left:433px">
    <div class="plan-head" style="background:var(--month-6)">6 MONTHS</div>
    <p class="plan-copy">Enjoy savings on fashion, beauty, restaurants and more for the next 6 months.</p>
    <p class="plan-price">Price: <b>£29.99</b><br>For 6 Months</p>
    <div class="plan-btn">BUY NOW</div>
  </article>

  <article class="abs plan" style="left:603px">
    <div class="plan-head" style="background:var(--month-12)">12 MONTHS</div>
    <p class="plan-copy">Enjoy savings on fashion, beauty, restaurants and more for the next 12 months.</p>
    <p class="plan-price">Price: <b>£39.99</b><br>For 12 Months</p>
    <div class="plan-btn">BUY NOW</div>
  </article>

  <p class="abs footnote">*LumaPass holders will be given an exclusive reduced rate upgrade option during the<br>initial launch of the LumaPass BLACK</p>
</section>
<div class="abs section-rule" style="top:743px"></div>

<h2 class="abs intro">INTRODUCING<br>LUMAPASS</h2>

<footer class="abs footer">
  <p class="f" style="left:46px;top:18px">SIGN UP TO OUR DAILY EMAIL - Please enter the validation code: luma</p>
  <span class="f" style="left:46px;top:45px">Email:</span>
  <div class="field" style="left:77px;top:44px;width:179px">enter your email address</div>
  <span class="f" style="left:259px;top:45px">Code:</span>
  <div class="field code" style="left:290px;top:45px;width:75px">enter code</div>
  <div class="signup-btn" style="left:375px;top:45px;width:53px">Sign up</div>

  <p class="f" style="left:536px;top:18px">CONNECT WITH LUMAPASS:</p>
  <span class="social" style="left:540px"></span>
  <span class="social" style="left:571px"></span>
  <span class="social" style="left:602px"></span>
  <span class="social" style="left:633px"></span>
  <span class="social" style="left:664px"></span>
  <span class="social" style="left:694px"></span>
  <span class="social" style="left:725px"></span>

  <div class="f-rule"></div>
  <ul class="links" style="left:46px">
    <li>About Us</li><li>Contact</li><li>Using Your Card</li><li>Buy A LumaPass</li><li>Become A Partner</li>
  </ul>
  <ul class="links" style="left:232px">
    <li>Shipping</li><li>Terms</li><li>Privacy Policy</li><li>Press</li><li>FAQs</li>
  </ul>
  <div class="legal">
    <p>© LumaPass Ltd. All Rights Reserved.</p>
    <p style="margin-top:7px">The celebrities named or featured on luma-pass.co.uk have not endorsed, recommended or approved the items featured on site.</p>
  </div>
</footer>

</body>
</html>
```